Local Flower Farm Needs Business Card Design

I need business cards designed for a flower farm based in Eudora, Kansas.
Business Info:
We are a local cut flower farm located in Eudora, Kansas, founded by Darla Hoffstrom. What started as a passion for agriculture and search for more joy in daily life has blossomed into a small business dedicated to providing the community with beautiful, fresh, and sustainable flowers. We specialize in local, seasonal blooms, ensuring that every petal reflects the care and dedication we pour into our craft. Our mission is to deliver the highest quality flowers directly to our customers through local farmers markets and to florists who share our commitment to sustainability. Join us in celebrating the beauty of nature, one bloom at a time!
Contact Details:
Darla Hoffstrom
Owner
Phone 913-555-0147
Facebook: Lorabelle Quinn Blossoms
Instagram: @LorabelleQuinnBlossoms
Website: LorabelleQuinnBlossoms.example
Target Market(s)
Wholesale to Florists and Direct to Consumer via Farmers Market
Industry/Entity Type
Florist, Farm
Contact Information for Business Card
Name, Contact Info, Logo
Look and feel

```html
<!DOCTYPE html>
<html lang="en">
<head>
<meta charset="utf-8">
<title>Lorabelle Quinn Blossoms – Business Card</title>
<link rel="stylesheet" href="https://fonts.googleapis.com/css2?family=Montserrat:wght@400;500;700&display=swap">
<style>
  :root {
    --ink-teal: #0a2a30;
    --accent-teal: #1f5866;
    --rule-teal: #4f7f8a;
    --paper: #ffffff;
    --silver: #c9d1d3;
    --edge-grey: #b5b5b5;
    --text-dark: #1f2a2d;
    --backdrop: #e4e6e7;
  }
  * { box-sizing: border-box; margin: 0; padding: 0; }
  html, body { width: 1200px; height: 1200px; overflow: hidden; }
  body {
    background: var(--backdrop);
    font-family: "Montserrat", Arial, sans-serif;
    position: relative;
  }
  .card {
    position: absolute;
    left: 150px;
    width: 900px;
    height: 514px;
    border-radius: 34px;
    overflow: hidden;
    box-shadow: 0 6px 18px rgba(0,0,0,0.18);
  }
  .card--front { top: 64px; background: var(--paper); }
  .card--back  { top: 622px; background: var(--ink-teal); }

  .card__band { position: absolute; inset: 0; }

  .brand {
    position: absolute;
    display: flex;
    align-items: center;
    justify-content: center;
    text-align: center;
    border-radius: 50%;
    font-family: "Montserrat", Arial, sans-serif;
    font-weight: 500;
    letter-spacing: 0.18em;
    text-transform: uppercase;
    line-height: 1.5;
  }
  .brand--front {
    left: 548px; top: 28px;
    width: 196px; height: 196px;
    border: 1.5px solid var(--ink-teal);
    color: var(--ink-teal);
    font-size: 15px;
  }
  .brand--back {
    left: 305px; top: 112px;
    width: 290px; height: 290px;
    border: 2px solid var(--silver);
    color: var(--silver);
    font-size: 22px;
  }

  .divider {
    position: absolute;
    height: 1.5px;
    background: var(--rule-teal);
  }
  .divider--top { left: 170px; right: 70px; top: 242px; }
  .divider--contact { left: 60px; width: 300px; top: 352px; }

  .person { position: absolute; left: 60px; top: 270px; }
  .person__name {
    font-weight: 700;
    font-size: 30px;
    line-height: 36px;
    color: var(--accent-teal);
    letter-spacing: 0.02em;
    text-transform: uppercase;
  }
  .person__role {
    font-weight: 400;
    font-size: 24px;
    line-height: 30px;
    color: var(--text-dark);
  }

  .contact-list {
    position: absolute;
    left: 60px; top: 362px;
    list-style: none;
  }
  .contact-list__item {
    display: flex;
    align-items: center;
    gap: 14px;
    font-size: 21px;
    color: var(--text-dark);
    height: 36px;
  }
  .contact-list__icon { width: 26px; height: 26px; flex: none; }

  .website {
    position: absolute;
    right: 44px; top: 440px;
    font-size: 17px;
    line-height: 22px;
    color: var(--paper);
    letter-spacing: 0.02em;
    white-space: nowrap;
  }
</style>
</head>
<body>

<section class="card card--front" aria-label="Business card front">
  <svg class="card__band" width="900" height="514" viewBox="0 0 900 514" aria-hidden="true">
    <path d="M0 496 L420 496 C500 496 500 392 580 392 L900 392 L900 514 L0 514 Z" fill="var(--edge-grey)"/>
    <path d="M0 504 L440 504 C520 504 520 404 600 404 L900 404 L900 514 L0 514 Z" fill="var(--ink-teal)"/>
  </svg>

  <div class="brand brand--front">Lorabelle<br>Quinn<br>Blossoms</div>

  <div class="divider divider--top"></div>

  <div class="person">
    <p class="person__name">Darla Hoffstrom</p>
    <p class="person__role">Owner</p>
  </div>

  <div class="divider divider--contact"></div>

  <ul class="contact-list">
    <li class="contact-list__item">
      <svg class="contact-list__icon" viewBox="0 0 24 24" aria-hidden="true">
        <path fill="var(--accent-teal)" d="M6.6 10.8a15.1 15.1 0 0 0 6.6 6.6l2.2-2.2a1 1 0 0 1 1-.25 11.4 11.4 0 0 0 3.6.57 1 1 0 0 1 1 1V20a1 1 0 0 1-1 1A17 17 0 0 1 3 4a1 1 0 0 1 1-1h3.5a1 1 0 0 1 1 1c0 1.25.2 2.45.57 3.57a1 1 0 0 1-.25 1z"/>
      </svg>
      <span>913-555-0147</span>
    </li>
    <li class="contact-list__item">
      <svg class="contact-list__icon" viewBox="0 0 28 28" aria-hidden="true">
        <rect x="2" y="2" width="24" height="24" rx="6" fill="none" stroke="var(--accent-teal)" stroke-width="2.5"/>
      </svg>
      <span>Lorabelle Quinn Blossoms</span>
    </li>
    <li class="contact-list__item">
      <svg class="contact-list__icon" viewBox="0 0 28 28" aria-hidden="true">
        <rect x="2" y="2" width="24" height="24" rx="6" fill="none" stroke="var(--accent-teal)" stroke-width="2.5"/>
      </svg>
      <span>@LorabelleQuinnBlossoms</span>
    </li>
  </ul>

  <p class="website">LorabelleQuinnBlossoms.example</p>
</section>

<section class="card card--back" aria-label="Business card back">
  <div class="brand brand--back">Lorabelle<br>Quinn<br>Blossoms</div>
</section>

</body>
</html>
```